Talbern Learning Recruitment Business Cards

We need business cards designed for our growing recruitment business.
We have just launched our offices in Sydney Melbourne and have a well established business in Perth. We are a fun young firm that specialise in Early Years Education Recruitment.
Our vision mission values are below
Our Vision:
To be:
the single, nationally recognised leader in the Early Childhood Sector.
a multifaceted organisation with a network of expertly driven facilities in the Early Childhood Sector, acknowledged as an organisation of integrity, innovation, heart and community.

Our Mission:
To provide superior quality recruitment services and solutions to the Early Childhood sector.
We empower our candidates to succeed.
We engage in trusted partnerships with our clients.
We grow our business/network/community, with passion and integrity.

Our Values:

We… are REAL
think: CUSTOMER
find: SOLUTIONS
achieve: RESULTS
enjoy: WHAT WE DO

Our website is www.talbernlearning.com feel free to visit it for inspiration.
Name Felix Ormsby
Title National Director
1300 057 812
0462 315 706
felix@talbernstaffing.com
website www.talbernlearning.com

I have attached our current business cards and logo designs to view

Target Market(s)

Recruitment

Industry/Entity Type

Business

Contact Information for Business Card

Name Felix Ormsby
Title National Director
1300 057 812
0462 315 706

Font styles to use
Serif

Requirements
Must have
• Company Values and the cities we have offices in Perth | Sydney | Melbourne
Nice to have
• Our Vision on the card
• Our Vision:
• To be a nationally recognised leader in the Early Childhood Sector.
• A multifaceted organisation with a network of expertly driven facilities in the Early Childhood Sector, acknowledged as an organisation of integrity, innovation, heart and community.

```html
<!DOCTYPE html>
<html lang="en">
<head>
<meta charset="utf-8">
<title>Talbern Learning Recruitment – Business Cards</title>
<link href="https://fonts.googleapis.com/css2?family=Montserrat:wght@400;500&display=swap" rel="stylesheet">
<style>
  :root {
    --page: #e7e4df;
    --navy: #123a63;
    --navy-deep: #14406b;
    --sky: #2a93c8;
    --accent: #2a9fd9;
    --white: #ffffff;
    --faint: rgba(255,255,255,0.13);
  }
  * { margin: 0; padding: 0; box-sizing: border-box; }
  html, body { width: 1200px; height: 843px; overflow: hidden; }
  body {
    background: var(--page);
    font-family: "Montserrat", sans-serif;
    position: relative;
  }
  .card {
    position: absolute;
    top: 252px;
    width: 558px;
    height: 319px;
    border-radius: 12px;
    overflow: hidden;
    box-shadow: 0 6px 16px rgba(0,0,0,0.25);
  }
  .card-front { left: 28px; background: var(--navy); }
  .card-back {
    left: 614px;
    background: linear-gradient(90deg, var(--navy-deep) 0%, #1b5a8c 45%, var(--sky) 100%);
  }
  .card-art { position: absolute; inset: 0; }
  .line {
    position: absolute;
    right: 25px;
    white-space: nowrap;
    text-align: right;
    color: var(--white);
    line-height: 1;
  }
  .holder-name { top: 70px; font-size: 24px; color: var(--accent); letter-spacing: 0.5px; }
  .holder-title { top: 101px; font-size: 14.5px; }
  .contact { font-size: 14.5px; display: flex; align-items: center; gap: 5px; }
  .contact svg { width: 10px; height: 10px; }
  .phone-office { top: 124px; }
  .phone-mobile { top: 142px; }
  .email { top: 159px; }
  .web { top: 177px; }
  .offices { top: 195px; font-size: 14.5px; color: var(--accent); }
  .social {
    position: absolute;
    display: flex;
    gap: 18px;
  }
  .social span {
    width: 15px; height: 15px; border-radius: 50%;
    background: var(--accent);
  }
  .card-front .social { right: 22px; top: 219px; }
  .card-back .social { right: 20px; top: 255px; }
  .card-back .social span { background: #123a63; opacity: 0.75; }
  .logo-name {
    position: absolute;
    left: 42px; top: 130px;
    width: 160px;
    text-align: center;
    color: var(--accent);
    font-size: 17px;
    font-weight: 500;
    line-height: 1.2;
  }
  .brand {
    position: absolute;
    left: 277px; top: 50px;
    color: var(--white);
    font-size: 22px;
    letter-spacing: 0.6px;
    white-space: nowrap;
  }
  .tagline {
    position: absolute;
    left: 288px; top: 81px;
    color: var(--white);
    font-size: 12px;
    font-weight: 500;
    white-space: nowrap;
  }
  .card-back .line { right: 18px; font-size: 14.5px; }
  .values-heading { top: 119px; font-weight: 500; font-size: 14.5px; }
  .values-1 { top: 137px; }
  .values-2 { top: 155px; }
  .values-2 .dot, .values-1 .dot { color: var(--accent); }
  .vision { top: 178px; line-height: 17.5px !important; font-size: 14.2px !important; }
</style>
</head>
<body>

<section class="card card-front">
  <svg class="card-art" viewBox="0 0 558 319" aria-hidden="true">
    <defs>
      <linearGradient id="ringFront" x1="0" y1="0" x2="0" y2="1">
        <stop offset="0" stop-color="#2aa4de"/>
        <stop offset="1" stop-color="#123a63"/>
      </linearGradient>
    </defs>
    <circle cx="519" cy="159" r="101" fill="none" stroke="var(--faint)" stroke-width="6"/>
    <circle cx="60.5" cy="160" r="194" fill="none" stroke="#2a9ad6" stroke-width="3"/>
    <circle cx="60.5" cy="160" r="189.5" fill="#ffffff"/>
    <circle cx="122" cy="157" r="88" fill="none" stroke="url(#ringFront)" stroke-width="5"/>
  </svg>
  <div class="logo-name">Talbern<br>Learning</div>

  <div class="line holder-name">FELIX ORMSBY</div>
  <div class="line holder-title">National Director</div>
  <div class="line contact phone-office">1300 057 812
    <svg viewBox="0 0 10 10"><path d="M2 1l2 2-1 1.3c.6 1.2 1.5 2.1 2.7 2.7L7 6l2 2-1.2 1.2C4.5 9 1 5.5.8 2.2z" fill="#2a9fd9"/></svg>
  </div>
  <div class="line contact phone-mobile">0462 315 706
    <svg viewBox="0 0 10 10"><rect x="2.5" y="0.5" width="5" height="9" rx="1" fill="none" stroke="#2a9fd9"/></svg>
  </div>
  <div class="line contact email">felix@talbernstaffing.com
    <svg viewBox="0 0 10 10"><rect x="0.5" y="2" width="9" height="6" fill="none" stroke="#2a9fd9"/><path d="M.5 2l4.5 3.5L9.5 2" fill="none" stroke="#2a9fd9"/></svg>
  </div>
  <div class="line contact web">www.talbernlearning.com
    <svg viewBox="0 0 10 10"><circle cx="5" cy="5" r="4.3" fill="none" stroke="#2a9fd9"/><path d="M.7 5h8.6M5 .7c-2.2 2.4-2.2 6.2 0 8.6M5 .7c2.2 2.4 2.2 6.2 0 8.6" fill="none" stroke="#2a9fd9" stroke-width=".8"/></svg>
  </div>
  <div class="line offices">Perth | Sydney | Melbourne</div>
  <div class="social"><span></span><span></span><span></span><span></span><span></span><span></span></div>
</section>

<section class="card card-back">
  <svg class="card-art" viewBox="0 0 558 319" aria-hidden="true">
    <circle cx="35" cy="159" r="118" fill="none" stroke="var(--faint)" stroke-width="6"/>
    <circle cx="212" cy="68" r="53" fill="none" stroke="#ffffff" stroke-width="4"/>
  </svg>
  <div class="brand">TALBERN LEARNING</div>
  <div class="tagline">Bringing quality to education recruitment</div>

  <div class="line values-heading">OUR VALUES:</div>
  <div class="line values-1">We... are REAL <span class="dot">•</span>Think: CUSTOMER <span class="dot">•</span>Find: SOLUTIONS</div>
  <div class="line values-2">Achieve: RESULTS <span class="dot">•</span>Enjoy: WHAT WE DO</div>
  <div class="line vision">To be a nationally recognised leader in the Early Childhood Sector.<br>
    A multifaceted organisation with a network of expertly driven facilities in<br>
    the Early Childhood Sector, acknowledged as an organisation of integrity,<br>
    innovation, heart and community.</div>
  <div class="social"><span></span><span></span><span></span><span></span><span></span><span></span></div>
</section>

</body>
</html>
```